I need a label created within the following dimensions below:

Label/Screen Printable Area:

Width 6.742”

Height 5.731”

The bottle dimensions are 7.175 (H) x 2.146 (D)
Updates

This is for 2 seperate labels.  One label for my hair Shampoo and another label for my hair Conditioner.

Requirements
Must have
• Front of Shampoo bottle:

Verdant Willow Crest logo

Product name (shampoo – Nourishing & Hydrating)

Bottle volume: 12 fl. Oz. (355ml)

Side of bottle:

"Herbal Strengthening with pure oil Essentials"

Back of bottle:

Verdant Willow Crest Shampoo is a blend of heavenly, ingredients from Mother Earth that nourish, protect and beautify your hair and extend the life of color. Our Products are Sulfate-Free, Paraben-Free, Contain No Artificial Colors and are Not Tested on Animals.

Distributed By and/or Get more information: (Distributed By: Willow Crest, Elmstead, OR 97410/ Get more information and connect with Willow Crest at www.verdantwillowcrestco.example)

Ingredients: (I’ve included the ingredients listings below for quick copying to your art file)

DESCRIPTION: Willow Crest Shampoo

How to/ Directions for use: (Apply to wet hair. Massage into a rich lather. Rinse. Repeat if necessary.)

INGREDIENTS: Purified Water, Sodium Methyl 2-Sulfolaurate & Disodium 2-Sulfolaurate & Cocamidopropyl Betaine, Cetrimonium Chloride, Distearyl Phthalic Acid Amide, Simmondsia Chinensis (Organic Jojoba Seed) Oil, Butyrospermum Parkii (Organic Shea Butter) Fruit, Aloe Barbadensis Leaf Juice (Organic Aloe Vera Gel), Hydrolyzed Quinoa (Protein), Dimethicone, Fragrance (Apple, Pear, White Grape), Gluconolactone & Sodium Benzoate (Natural Preservative), Panthenol (Vitamin B-5), Citric Acid, Tocopherol (Vitamin E).

Front of conditioner bottle:

Product name: (Conditioner Shampoo - luxurious volume conditioner)

Side of bottle:

Back of bottle:

DESCRIPTION: Willow Crest Restructurant Conditioner

How to/ Directions for use: (Apply to wet hair. Massage into hair and sit for 5 minutes. For a deep conditoner treatment apply to hair and sit under the hair dryer for 20-30 minutes, Repeat if necessary; then rinse and style as usual).

INGREDIENTS: Purified Water, Behentrimonium Methosulfate (Modified Rapseed Oil), Cetearyl Alcohol, Cetyl Alcohol, Cetrimonium Chloride, Cyclopentasiloxane and Dimethicone, Caprylic/Capric Triglyceride, Extracts of Foeniculum Vulgare (Fennel Seed) and Helianthus Annuus (Sunflower Seed), Simmondsia Chinensis (Jojoba Seed) Oil, Olea Europaea (Olive Fruit) Oil, Fragrance, Mentha Piperita (Peppermint) Oil, Mentha (Menthol), Aloe Barbadensis Leaf Juice (Organic Aloe Vera Gel), Hydrolyzed Hair Keratin, Butyrospermum Parkii (Organic Shea Butter) Fruit, Sodium Benzoate (Natural Preservative) and Potassium Sorbate, Rosmarinus Officinalis (Rosemary) Oil, Lavandula Officinalis (Lavender) Oil, Panthenol (Vitamin B-5), Tocopherol (Vitamin E), Guar Hydroxypropyltrimonium Chloride, Citric Acid.

Width 6.742”

Height 5.731”

Should not have
• No other colors then what my logo colors currently are.

```html
<!DOCTYPE html>
<html lang="en">
<head>
<meta charset="utf-8">
<title>Verdant Willow Crest – Nourishing &amp; Hydrating Shampoo Label</title>
<link rel="stylesheet" href="https://fonts.googleapis.com/css2?family=PT+Sans:ital,wght@0,400;0,700;1,400;1,700&display=swap">
<style>
  :root {
    --gold: #a77c22;
    --gold-light: #c39a3c;
    --green: #1f5a3a;
    --label: #fbfbf9;
    --backdrop: #ececea;
    --fold-line: #d9d6cc;
  }
  * { box-sizing: border-box; margin: 0; padding: 0; }
  html, body {
    width: 1200px; height: 900px; overflow: hidden;
    background: var(--backdrop);
    font-family: "PT Sans", Arial, sans-serif;
  }
  .label {
    position: absolute; left: 120px; top: 60px;
    width: 960px; height: 780px;
    background: var(--label);
    display: grid;
    grid-template-columns: 380px 380px 200px;
    box-shadow: 0 2px 10px rgba(0,0,0,.08);
  }
  .panel { position: relative; text-align: center; padding: 0 30px; }
  .panel + .panel { border-left: 1px dashed var(--fold-line); }

  /* Front */
  .front { display: flex; flex-direction: column; align-items: center; }
  .brand-mark {
    margin-top: 70px;
    display: flex; flex-direction: column; align-items: center; gap: 10px;
  }
  .brand-dot { width: 18px; height: 18px; border-radius: 50%; background: var(--gold); }
  .brand-name { color: var(--green); font-weight: 700; font-size: 30px; line-height: 1.05; }
  .illustration {
    margin-top: 46px; width: 200px; height: 170px;
    background: radial-gradient(ellipse at 50% 60%, #2f6b47 0%, #1f5a3a 55%, #b58a33 100%);
    border-radius: 40% 40% 8px 8px;
  }
  .product-line {
    margin-top: 42px; color: var(--gold);
    font-size: 27px; line-height: 1.05; text-transform: uppercase; letter-spacing: .3px;
  }
  .product-band {
    margin-top: 8px; width: 210px; padding: 4px 0;
    background: var(--gold); color: #fff;
    font-weight: 700; font-size: 26px; border-radius: 3px;
  }
  .tagline { margin-top: 10px; color: var(--green); font-style: italic; font-size: 16px; line-height: 1.15; }
  .tagline b { font-weight: 700; }
  .volume { position: absolute; bottom: 50px; left: 0; right: 0; color: var(--green); font-weight: 700; font-size: 16px; }

  /* Back */
  .back { padding-top: 70px; }
  .back .brand-mark { margin-top: 0; }
  .back .brand-name { font-size: 22px; }
  .back .brand-dot { width: 13px; height: 13px; }
  .back-title {
    margin-top: 22px; display: flex; justify-content: center; align-items: center; gap: 6px;
    color: var(--gold); font-size: 15px; line-height: 1.05; text-transform: uppercase; text-align: right;
  }
  .back-title .band { background: var(--gold); color: #fff; font-weight: 700; font-size: 20px; padding: 2px 8px; border-radius: 3px; }
  .description { margin-top: 10px; color: var(--gold); font-style: italic; font-weight: 700; font-size: 12.5px; line-height: 1.35; }
  .section-pill {
    display: inline-block; margin-top: 34px;
    background: var(--gold); color: #fff; font-weight: 700; font-style: italic;
    font-size: 13.5px; padding: 1px 10px; border-radius: 3px;
  }
  .section-pill.ingredients-pill { margin-top: 26px; }
  .body-copy { margin-top: 5px; color: var(--green); font-size: 11.5px; line-height: 1.35; }
  .distributor { margin-top: 36px; color: var(--green); font-size: 11.5px; line-height: 1.3; }
  .distributor .heading { color: var(--gold); font-weight: 700; font-style: italic; font-size: 14px; }
  .distributor .web { color: var(--gold); font-weight: 700; font-size: 12.5px; }

  /* Side */
  .side { display: flex; align-items: center; justify-content: center; }
  .side-tagline {
    writing-mode: vertical-rl; transform: rotate(180deg);
    color: var(--gold); font-style: italic; font-size: 30px; white-space: nowrap;
  }
  .side-tagline b { font-weight: 700; }
</style>
</head>
<body>
<main class="label">
  <section class="panel front">
    <div class="brand-mark">
      <span class="brand-dot"></span>
      <span class="brand-name">Verdant Willow Crest</span>
    </div>
    <div class="illustration" role="img" aria-label="Illustration of an aloe vera plant with two golden flower buds"></div>
    <p class="product-line">Nourishing &amp;<br>Hydrating</p>
    <p class="product-band">SHAMPOO</p>
    <p class="tagline">Herbal Strengthening<br>with <b>Pure Oil</b> Essentials</p>
    <p class="volume">12 fl. Oz. (355ml)</p>
  </section>

  <section class="panel back">
    <div class="brand-mark">
      <span class="brand-dot"></span>
      <span class="brand-name">Verdant Willow Crest</span>
    </div>
    <div class="back-title"><span>Nourishing<br>&amp; Hydrating</span><span class="band">SHAMPOO</span></div>
    <p class="description">Verdant Willow Crest Shampoo is a blend of heavenly, ingredients from Mother Earth that nourish, protect and beautify your hair and extend the life of color. Our Products are Sulfate-Free, Paraben-Free, Contain No Artificial Colors and are Not Tested on Animals.</p>

    <span class="section-pill">Directions for use</span>
    <p class="body-copy">Apply to wet hair. Massage into a rich lather.<br>Rinse. Repeat if necessary</p>

    <span class="section-pill ingredients-pill">Ingredients</span>
    <p class="body-copy">Purified Water, Sodium Methyl 2-Sulfolaurate &amp; Disodium 2-Sulfolaurate &amp; Cocamidopropyl Betaine, Cetrimonium Chloride, Distearyl Phthalic Acid Amide, Simmondsia Chinensis (Organic Jojoba Seed) Oil, Butyrospermum Parkii (Organic Shea Butter) Fruit, Aloe Barbadensis Leaf Juice (Organic Aloe Vera Gel), Hydrolyzed Quinoa (Protein), Dimethicone, Fragrance (Apple, Pear, White Grape), Gluconolactone &amp; Sodium Benzoate (Natural Preservative), Panthenol (Vitamin B-5), Citric Acid, Tocopherol (Vitamin E).</p>

    <div class="distributor">
      <p class="heading">Distributed By</p>
      <p>Willow Crest, Elmstead, OR 97410<br>Get more information and connect<br>with Willow Crest at</p>
      <p class="web">www.verdantwillowcrestco.example</p>
    </div>
  </section>

  <section class="panel side">
    <p class="side-tagline">Herbal Strengthening with <b>Pure Oil</b> Essentials</p>
  </section>
</main>
</body>
</html>
```